Summer Camp Flyer Design Project

I need a double-sided flyer (letter size) to advertize our Summer Camp. It is a day camp for children ages 3 years to 12 years, hosted at our school, where participating students play sports, work on Math and their reading/writing skills, learn and practice either of Tabla, Keertan (devotional spiritual music), or painting. Once a week, we take the children to a trip into nature, to watch a movie, or to a farm. See details of program on: http://www.trelvoacademy.org/index.php?option=com_content&view=article&id=95&Itemid=58

The flyer should give the impression that this will be a fun program where the children will learn as well.

I am attaching a flyer I created for our last year's program. I am hoping the magical designers in the design crowd can really demonstrate the value of professional work vs my amateur effort.

I am also attaching some pics that can be used or you could put some nice pics that you might have.
Updates

Just sent this feedback to a designer:

Your page 1 is so nice! Thanks. This second page needs changes. Instead of the headings Montessori, Math..etc...I would like to see PLAY, LEARN, Pick a TALENT, Have FUN!. The four pictures can be replaced by pictures appropriate for each of these headings. Take a look at http://trelvoacademy.org/index.php?option=com_content&view=article&id=95&Itemid=58

PLAY
You will start your day with outdoor sports - Soccer, Frisbee games, Athletic games - the fresh air, the exercise, and the enthusiastic coaches will give you a time your body will thank you for.

LEARN
Discover the joy of learning. Effortlessly and joyfully get a step ahead of your classmates in Math and English. With one-on-one tutoring and customized lessons, get a step ahead of your class. We have scientific assessment tools to give you measurable progress. Learn Punjabi, connect with your history and faith.

PICK A TALENT
Have you been learning Tabla but you still can't get the right sound and clarity in your performance? Practice everyday with Ustad Baldev Rao, a student of Ustad Mehran Qadri. May be your interest is in Visual Arts. Learn the tricks to create your own masterpiece! We also have Keertan lessons for those interested in learning new Shabads.

HAVE FUN!
Summer has to be fun! We have packed more fun in a day for you than ever before. Your day with us ends with non-competitive, just for fun games. Everybody wins and everybody goes home with a big smile.

Target Market(s)

East Indian Parents of children ages 3 years to 12 years

Industry/Entity Type

Movie

Requirements
Must have
• pics depicting nature, children studying, painting, playing soccer, having fun, and one for tabla

dates of program: July 2 - July 26

timings: 9:00am to 3:30pm; after school day care till 5:00pm

```html
<!DOCTYPE html>
<html lang="en">
<head>
<meta charset="utf-8">
<title>Summer Camp — Play, Learn, Pick a Talent, Have Fun</title>
<link rel="stylesheet" href="https://fonts.googleapis.com/css2?family=Comfortaa:wght@300;400&family=Poiret+One&display=swap">
<style>
  :root{
    --sun:#ffdf1f;
    --royal:#1f1fe0;
    --violet:#7434d8;
    --scarlet:#ef1f1f;
    --lime:#4fe11a;
    --text-sun:#ffe23a;
    --text-amber:#ffd21a;
    --text-violet:#7a2fd8;
    --text-green:#5ef22a;
    --white:#ffffff;
    --photo-warm:#b89a86;
    --photo-cool:#5a4a6a;
  }
  *{box-sizing:border-box;margin:0;padding:0}
  html,body{width:926px;height:1200px;overflow:hidden;background:var(--sun)}
  .flyer{position:relative;width:926px;height:1200px;background:var(--sun);overflow:hidden;
    font-family:"Comfortaa",sans-serif;font-weight:300}
  .block{position:absolute}
  .copy{position:absolute;text-align:center;line-height:1.22}
  .time{display:block;font-size:13px;margin-bottom:6px}
  .heading{position:absolute;font-family:"Poiret One","Comfortaa",sans-serif;line-height:1}

  .price{left:27px;top:45px;width:200px;height:73px;background:var(--scarlet)}
  .price p{color:var(--text-sun);font-size:15px;line-height:1.25;text-align:center;padding-top:16px}

  .play-panel{left:227px;top:12px;width:658px;height:230px;background:var(--royal);
    clip-path:polygon(0 6%,100% 0,99% 100%,1% 96%)}
  .play-tab{left:0;top:135px;width:250px;height:92px;background:var(--royal)}
  .play-tab .heading{left:42px;top:12px;font-size:72px;color:var(--scarlet)}
  .play-copy{left:260px;top:28px;width:600px;color:var(--text-sun);font-size:24px;transform:rotate(-2deg)}

  .photo{position:absolute}
  .photo-study{left:439px;top:227px;width:487px;height:212px;
    background:linear-gradient(120deg,#efe9e2 0%,var(--photo-warm) 45%,#3b3550 100%)}
  .photo-tabla{left:0;top:530px;width:484px;height:211px;
    background:linear-gradient(100deg,var(--photo-cool) 0%,#2b3a7a 40%,#c9ccd8 100%)}

  .learn-panel{left:53px;top:242px;width:613px;height:356px;background:var(--violet);
    clip-path:polygon(0 0,100% 8%,100% 100%,0 94%)}
  .learn-copy{left:70px;top:270px;width:585px;color:var(--text-amber);font-size:24px;transform:rotate(3deg)}
  .learn-tab{left:598px;top:439px;width:310px;height:121px;background:var(--violet);
    clip-path:polygon(0 0,100% 10%,100% 100%,0 92%)}
  .learn-tab .heading{left:50px;top:22px;font-size:78px;color:var(--text-green)}

  .arrow{position:absolute;left:370px;top:585px;width:300px;height:50px}

  .talent-panel{left:280px;top:583px;width:613px;height:287px;background:var(--scarlet);
    clip-path:polygon(0 6%,100% 0,100% 100%,2% 96%)}
  .talent-copy{left:305px;top:648px;width:570px;color:var(--text-violet);font-size:24px;transform:rotate(-1.5deg)}
  .talent-tab{left:15px;top:753px;width:288px;height:125px;background:var(--scarlet)}
  .talent-tab .small{left:103px;top:18px;font-size:22px;color:var(--text-sun)}
  .talent-tab .big{left:16px;top:44px;font-size:72px;color:var(--text-sun)}

  .violet-wedge{left:688px;top:847px;width:238px;height:167px;background:var(--violet);
    clip-path:polygon(0 0,100% 0,100% 100%,4% 100%)}

  .fun-panel{left:30px;top:893px;width:651px;height:307px;background:var(--lime);
    clip-path:polygon(0 0,100% 4%,99% 100%,1% 100%)}
  .fun-copy{left:55px;top:922px;width:600px;color:var(--text-sun);font-size:24px;transform:rotate(2deg)}
  .fun-tab{left:681px;top:1014px;width:227px;height:113px;background:var(--lime)}
  .fun-tab .small{left:40px;top:14px;font-size:26px;color:var(--white)}
  .fun-tab .big{left:30px;top:40px;font-size:72px;color:var(--white)}
</style>
</head>
<body>
<main class="flyer">

  <div class="block price"><p>starting from 160/week<br>Registar Online!</p></div>

  <div class="block play-panel"></div>
  <div class="block play-tab"><h2 class="heading">PLAY</h2></div>
  <p class="copy play-copy"><span class="time">9:00AM -10:00AM</span>You will start your day with outdoor sports - Soccer, Frisbee games, Athletic games - the fresh air, the exercise, and the enthusiastic coaches will give you a time your body will thank you for.</p>

  <div class="photo photo-study" role="img" aria-label="Photo of a young boy in a white patka resting his chin on his hand while studying"></div>

  <div class="block learn-panel"></div>
  <p class="copy learn-copy"><span class="time">10:30AM -12:30PM</span>Get a step ahead of your classmates in Math and English. We offer one-on-one tutoring and customized lessons.We have scientific assessment tools to give you measurable progress. Learn Punjabi, connect with your history and faith.</p>
  <div class="block learn-tab"><h2 class="heading">LEARN</h2></div>

  <div class="photo photo-tabla" role="img" aria-label="Photo of the tabla teacher performing at a recognition event"></div>

  <div class="block talent-panel"></div>
  <svg class="arrow" viewBox="0 0 300 50" aria-hidden="true">
    <path d="M290 12 C220 2 120 4 20 30" fill="none" stroke="#ef1f1f" stroke-width="3"/>
    <path d="M20 30 L34 18 M20 30 L37 36" fill="none" stroke="#ef1f1f" stroke-width="3" stroke-linecap="round"/>
  </svg>
  <p class="copy talent-copy"><span class="time">1:30PM-2:30PM</span>Practice everyday with Ustad Baldev Rao, a student of Ustad Mehran Qadri. May be your interest is in Visual Arts. We also have Keertan lessons for those interested in learning new Shabads</p>
  <div class="block talent-tab">
    <span class="heading small">PICK A</span>
    <h2 class="heading big">TALENT</h2>
  </div>

  <div class="block violet-wedge"></div>

  <div class="block fun-panel"></div>
  <p class="copy fun-copy"><span class="time">2:30PM-3:30PM</span>Summer has to be fun! We have packed more fun in a day for you than ever before. Your day with us ends with non-competitive,just for fun games. Everybody wins and everybody goes home with a big smile.</p>
  <div class="block fun-tab">
    <span class="heading small">HAVE</span>
    <h2 class="heading big">FUN</h2>
  </div>

</main>
</body>
</html>
```